We are energy brokers. www.brightvalecurrent.com
We are inviting auto dealers to participate in an energy buyers group that will help them reduce their cost of electricity.
I would like something that can be easily traded out for other industries. ie Gym Owners buyers group, New Business buyers group, etc.
rob@brightvalecurrent.com
855.417.3096 phone

I need this to specifically target "Auto Dealers Energy Buying Group"  
We are targeting only Automobile dealers with this campaign.  Perhaps use a graphic that depicts an auto dealership at night.  Similar to this one.
http://lumenwharfdepot.com/wp-content/uploads/2012/04/auto-dealer-lighting-banner7.jpg

Please use these bullet points:

-Be part of the areas largest Auto Dealers Energy Buying Group
-Reduce energy costs significantly
-Local and professional energy brokers who you can trust
-Free LED lighting analysis available
-Send your latest bill to rob@brightvalecurrent.com to get started

Target Market(s)

Auto Dealers.

Industry/Entity Type

Business

Requirements
Must have
• Brightvale Current logo.
Reduced energy costs equals greater profits.
Free Lighting Analysis.
Energy Costs are at 12 year lows. Great rates available.
Free phone consultation.
http://s21.beta.snapvaultimg.com/user/robertkolm/media/HHUb.png.html This chart depicts natural gas. Gas determines where energy prices are going. This shows natural gas is cheap right now.

```html
<!DOCTYPE html>
<html lang="en">
<head>
<meta charset="utf-8">
<title>Brightvale Current – Auto Dealers Energy Buying Group</title>
<link rel="stylesheet" href="https://fonts.googleapis.com/css2?family=EB+Garamond:wght@400;600;700&family=Open+Sans:wght@400&display=swap">
<style>
  :root {
    --paper: #ffffff;
    --brand-green: #1a9a4a;
    --band-green: #0e9546;
    --bullet-yellow: #f4ef1c;
    --text-light: #ffffff;
    --text-dark: #111111;
  }
  * { margin: 0; padding: 0; box-sizing: border-box; }
  html, body { width: 872px; height: 1200px; overflow: hidden; background: var(--paper); }
  .flyer { position: relative; width: 872px; height: 1200px; background: var(--paper); font-family: "EB Garamond", Garamond, serif; }
  .backdrop { position: absolute; inset: 0; }
  .brand { position: absolute; left: 80px; top: 42px; display: flex; align-items: center; gap: 14px; }
  .brand-mark { width: 46px; height: 46px; background: var(--brand-green); }
  .brand-name { font-family: "Open Sans", Arial, sans-serif; font-weight: 400; font-size: 40px; color: var(--brand-green); letter-spacing: -0.5px; }
  .invite { position: absolute; left: 0; width: 872px; top: 192px; text-align: center; color: var(--text-light); text-shadow: 0 1px 3px rgba(0,0,0,.6); }
  .invite-lead { font-size: 31px; font-weight: 700; line-height: 32px; }
  .invite-lead span { display: block; }
  .invite-title { font-size: 42px; font-weight: 600; line-height: 54px; margin-top: 4px; letter-spacing: .2px; }
  .benefits { position: absolute; left: 328px; top: 522px; width: 500px; list-style: none; color: var(--text-light); font-weight: 700; font-size: 30px; line-height: 34px; }
  .benefits li { position: relative; padding-left: 20px; margin-bottom: 18px; }
  .benefits li::before { content: ""; position: absolute; left: 0; top: 11px; width: 10px; height: 10px; background: var(--bullet-yellow); }
  .contact { position: absolute; left: 0; width: 872px; top: 1044px; text-align: center; color: var(--text-dark); }
  .contact-lead { font-size: 30px; line-height: 36px; }
  .contact-email { font-size: 28px; font-weight: 700; line-height: 36px; }
  .contact-phone { font-size: 44px; font-weight: 600; line-height: 58px; }
</style>
</head>
<body>
<main class="flyer">
  <svg class="backdrop" width="872" height="1200" viewBox="0 0 872 1200">
    <defs>
      <linearGradient id="header-fade" x1="0" y1="0" x2="0" y2="1">
        <stop offset="0" stop-color="#ffffff"/>
        <stop offset="1" stop-color="#dff1f7"/>
      </linearGradient>
      <linearGradient id="dealership-night" x1="0" y1="0" x2="1" y2="1">
        <stop offset="0" stop-color="#2a4a9a"/>
        <stop offset="0.45" stop-color="#1b2d66"/>
        <stop offset="1" stop-color="#15161e"/>
      </linearGradient>
      <radialGradient id="sunlit-sky" cx="0.2" cy="0.25" r="0.9">
        <stop offset="0" stop-color="#e8f2ff"/>
        <stop offset="0.12" stop-color="#6da2e4"/>
        <stop offset="0.45" stop-color="#1f4aa6"/>
        <stop offset="1" stop-color="#0a1462"/>
      </radialGradient>
    </defs>
    <rect x="22" y="0" width="840" height="140" fill="url(#header-fade)"/>
    <g role="img" aria-label="Auto dealership lit up at night">
      <path d="M22 120 Q300 95 560 108 Q760 118 862 110 L862 388 Q700 370 540 380 Q300 395 22 378 Z" fill="url(#dealership-night)"/>
    </g>
    <path d="M22 378 Q300 395 540 380 Q700 370 862 388 L862 478 Q600 495 400 478 Q200 462 22 470 Z" fill="var(--band-green)"/>
    <path d="M22 378 Q300 395 540 380 Q700 370 862 388" fill="none" stroke="#ffffff" stroke-width="3"/>
    <path d="M22 470 Q200 462 400 478 Q600 495 862 478" fill="none" stroke="#ffffff" stroke-width="3"/>
    <g role="img" aria-label="Bright sun shining in a deep blue sky with a wisp of cloud">
      <path d="M22 472 Q200 464 400 480 Q600 497 862 480 L862 1020 Q700 1030 500 1015 Q300 995 22 1030 Z" fill="url(#sunlit-sky)"/>
    </g>
  </svg>

  <header class="brand">
    <span class="brand-mark"></span>
    <span class="brand-name">brightvalecurrent</span>
  </header>

  <section class="invite">
    <p class="invite-lead"><span>You are invited</span><span>to participate in an</span></p>
    <h1 class="invite-title">Auto Dealers Energy Buying Group</h1>
  </section>

  <ul class="benefits">
    <li>Be part of the area's largest Auto Dealers Energy Buying Group.</li>
    <li>Reduce energy costs significantly.</li>
    <li>Local and professional energy brokers who you can trust.</li>
    <li>Free LED lighting analysis available.</li>
    <li>Send your latest bill to rob@brightvalecurrent.com to get started.</li>
  </ul>

  <footer class="contact">
    <p class="contact-lead">For more information contact</p>
    <p class="contact-email">rob@brightvalecurrent.com</p>
    <p class="contact-phone">855.417.3096</p>
  </footer>
</main>
</body>
</html>
```